One pager digital ad-Corporate travel Manager

I need a design that is smooth, and business like. I don’t like basic generic designs that I can make my self. I’m looking for a sharp clean ad that clearly was made by a great designer. I need some bullet points in and the add to be clean. Here is a list of some content from our content writers. You can arrange and play with the words a bit.

*Budget*- having a travel management service will ensure that your company sticks to a budget which will help PROTECT your bottom line. Travel expenses often CAN BE COSTLY and having a SAVVY corporate travel manager handle YOUR TRAVEL ARRANGEMENTS will make sure that the travel expenses are kept under control.
*Efficiency- time *is money. Have your staff focus on their core business and have the corporate travel manager handle all the logistics for their travel including airfare, hotel cars and events TO MAXIMIZE EFFICIENCY AND KEEP YOUR STAFF FOCUSED ON YOUR CORE BUSINESS

*unforeseen circumstances* – the corporate travel manager handleS any cancellations, missed flights, canceled flights. Quick rebooking, and repositioning, and dealing with getting credits and reimbursement is extremely difficult and time-consuming. The corporate travel manager handles all of that SO YOU CAN CONTINUE ON SCHEDULE WITHOUT SPENDING HOURS REBOOKING AND GETTING CREDIT

Efficient and organized business travel management-help reduce travel expenses, streamline expense reports, optimize booking processes, and make managing the corporate travel experience way easier for all stakeholders involved.

Travel Support

Report on travel spend: In order to optimize their budgets, businesses need to know which departments are spending what on travel. Agencies can report on spend for all stakeholders by team, department, or project, and help you accurately track all your travel expenses.

Maintain compliance: Every company has some sort of rules that make up their travel policy. An agency can enforce these guidelines when booking.

Velmora Journeys is a global leader in business travel management services. We drive savings, efficiency and safety to businesses and their travelers all around the world.

If you are looking for a tailored travel management solution, delivering customer service excellence, and a demonstrable return on investment, then you’ve come to the right place

Corporate travel policy compliance
Travel management reports
Meetings and event management
Travel program management
Dedicated travel counselor teams

By listening to your needs and focusing on your goals we can help your company design a global corporate travel service program that controls costs, improves traveler satisfaction and fits your corporate culture.

Our qualified business travel agents and cutting-edge technology deliver solutions that provide the best travel arrangements and travel policy adherence in the business. From CEO to support staff, our services can help make corporate travel a more efficient and enjoyable experience for everyone involved.

With so much involved in travel – from booking and expenses to meetings and strategy – you need the backing of a proven leader…
Velmora Journeys, We’re your corporate travel partner to help you manage it all.

```html
<!DOCTYPE html>
<html lang="en">
<head>
<meta charset="utf-8">
<title>Velmora Journeys – Business Travel Reinvented</title>
<link rel="stylesheet" href="https://fonts.googleapis.com/css2?family=Didact+Gothic&family=Montserrat:wght@300;400&display=swap">
<style>
  :root{
    --page-bg:#e9e9ea;
    --navy:#0b1833;
    --navy-deep:#081226;
    --crimson:#c0183a;
    --wine:#5a1a3c;
    --cyan:#2bb7ea;
    --ink:#e9eef5;
    --body-font:"Didact Gothic", "Montserrat", sans-serif;
    --display-font:"Montserrat", sans-serif;
  }
  *{box-sizing:border-box;margin:0;padding:0}
  html,body{width:1200px;height:1157px;overflow:hidden;background:var(--page-bg)}
  .ad{
    position:absolute;left:171px;top:0;width:857px;height:1157px;
    background:var(--navy);color:var(--ink);font-family:var(--body-font);overflow:hidden;
  }
  .hero-photo{
    position:absolute;left:0;top:0;width:100%;height:270px;
    background:
      radial-gradient(ellipse 60% 45% at 55% 30%, rgba(220,30,60,.95), rgba(192,24,58,0) 70%),
      linear-gradient(180deg,#8c1834 0%,var(--crimson) 35%,var(--wine) 70%,var(--navy) 100%);
  }
  .footer-glow{
    position:absolute;left:0;bottom:0;width:100%;height:150px;
    background:linear-gradient(180deg,rgba(11,24,51,0) 0%,#6a1a3d 55%,#3a1433 78%,var(--navy-deep) 100%);
  }
  .brand{position:absolute;top:190px;left:0;width:100%;text-align:center}
  .brand-name{font-family:var(--display-font);font-weight:300;font-size:27px;letter-spacing:4px;text-transform:uppercase;color:var(--ink)}
  .brand-tagline{margin-top:5px;font-family:var(--display-font);font-size:11px;letter-spacing:8.5px;text-transform:uppercase;color:var(--ink)}

  .block{position:absolute}
  .section-title{
    display:flex;align-items:center;gap:6px;
    font-family:var(--display-font);font-size:12px;letter-spacing:1.6px;color:var(--cyan);text-transform:uppercase;
  }
  .section-title::before,.section-title::after{content:"";flex:1;height:1px;background:var(--cyan)}
  .copy{font-size:10.6px;line-height:13.2px;text-align:justify;text-align-last:left}
  .copy .accent,.subhead{color:var(--cyan)}
  .subhead{display:block}
  .col-left{left:70px;width:342px}
  .col-right{left:447px;width:340px}
  .full{left:70px;width:717px}

  .intro{position:absolute;left:0;width:100%;text-align:center;font-size:15.5px;line-height:18px}
  .intro .lead{color:var(--ink);text-transform:uppercase;font-size:14px}
  .intro .cyan{color:var(--cyan)}
  .services{position:absolute;top:800px;left:0;width:100%;text-align:center;list-style:none;font-size:17px;line-height:23.5px;color:var(--cyan)}
  .services li{display:inline}
  .services li::before{content:"• ";font-size:12px}
  .services .break{display:block;height:0}
  .closing{position:absolute;top:997px;left:0;width:100%;text-align:center;font-size:15px;line-height:19px}
  .signoff{position:absolute;top:1072px;left:0;width:100%;text-align:center}
  .signoff-name{font-family:var(--body-font);font-size:25px;color:var(--cyan);text-transform:uppercase;letter-spacing:.5px}
  .signoff-line{font-size:14.5px;margin-top:-2px}
</style>
</head>
<body>
<main class="ad">
  <div class="hero-photo" role="img" aria-label="Silhouette of a passenger jet landing against a crimson sunset sky"></div>
  <div class="footer-glow" role="img" aria-label="Red sunset horizon over dark clouds"></div>

  <header class="brand">
    <h1 class="brand-name">Velmora Journeys</h1>
    <p class="brand-tagline">Business Travel Reinvented</p>
  </header>

  <section class="block col-left" style="top:282px">
    <h2 class="section-title">Budget</h2>
    <p class="copy" style="margin-top:5px">having a travel management service will ensure that your company sticks to a budget which will help PROTECT your bottom line. Travel expenses often CAN BE COSTLY and having a SAVVY corporate travel manager handle YOUR TRAVEL ARRANGEMENTS will make sure that the travel expenses are kept under control.</p>
  </section>

  <section class="block col-right" style="top:282px">
    <h2 class="section-title">Efficiency</h2>
    <p class="copy" style="margin-top:5px">Time *is money. Have your staff focus on their core business and have the corporate travel manager handle all the logistics for their travel including airfare, hotel cars and events TO MAXIMIZE EFFICIENCY AND KEEP YOUR STAFF FOCUSED ON YOUR CORE BUSINESS</p>
  </section>

  <h2 class="block full section-title" style="top:392px">Unforeseen Circumstances</h2>
  <p class="block col-left copy" style="top:414px">The corporate travel manager handles any cancellations, missed flights, canceled flights. Quick rebooking, and repositioning, and dealing with getting credits and reimbursement is extremely difficult and time-consuming. The corporate travel manager handles all of that <span class="accent">SO YOU CAN CONTINUE ON SCHEDULE WITHOUT SPENDING HOURS REBOOKING AND GETTING CREDIT.</span></p>
  <p class="block col-right copy" style="top:414px"><span class="subhead">Efficient and organized business travel management</span>Help reduce travel expenses, streamline expense reports, optimize booking processes, and make managing the corporate travel experience way easier for all stakeholders involved.</p>

  <h2 class="block full section-title" style="top:520px">Travel Support</h2>
  <p class="block col-left copy" style="top:543px"><span class="subhead">Report on travel spend:</span>In order to optimize their budgets, businesses need to know which departments are spending what on travel. Agencies can report on spend for all stakeholders by team, department, or project, and help you accurately track all your travel expenses.</p>
  <p class="block col-right copy" style="top:543px"><span class="subhead">Maintain compliance:</span>Every company has some sort of rules that make up their travel policy. An agency can enforce these guidelines when booking.</p>

  <div class="intro" style="top:648px">
    <p class="lead">Velmora Journeys</p>
    <p class="cyan">is a global leader in business travel management services. We drive savings,<br>efficiency and safety to businesses and their travelers all around the world.</p>
    <p class="cyan" style="margin-top:15px">If you are looking for a tailored travel management solution, delivering customer service<br>excellence, and a demonstrable return on investment,</p>
    <p class="lead" style="margin-top:4px">Then you’ve come to the right place.</p>
  </div>

  <ul class="services">
    <li>Corporate travel policy compliance</li> <li>Travel management reports</li><span class="break"></span>
    <li>Meetings and event management</li> <li>Travel program management</li><span class="break"></span>
    <li>Dedicated travel counselor teams</li>
  </ul>

  <p class="block full copy" style="top:889px">By listening to your needs and focusing on your goals we can help your company design a global corporate travel service program that controls costs, improves traveler satisfaction and fits your corporate culture.</p>
  <p class="block full copy" style="top:928px">Our qualified business travel agents and cutting-edge technology deliver solutions that provide the best travel arrangements and travel policy adherence in the business. From CEO to support staff, our services can help make corporate travel a more efficient and enjoyable experience for everyone involved.</p>

  <p class="closing">With so much involved in travel<br>from booking and expenses to meetings and strategy<br>you need the backing of a proven leader…</p>

  <footer class="signoff">
    <p class="signoff-name">Velmora Journeys</p>
    <p class="signoff-line">We’re your corporate travel partner to help you manage it all.</p>
  </footer>
</main>
</body>
</html>
```